Love pets? Create a veterinary business card that aligns with our new revamped website.

Greetings! We are a five-doctor veterinary hospital that seeks your expertise in designing a new business card that harmonizes with our recently revitalized website: www.lmcr.net. The card should feature our logo, the five doctors, operating hours, contact information, and communicate our purpose and personality.

Contact Information for Business Card

TBA

```html
<!DOCTYPE html>
<html lang="en">
<head>
<meta charset="utf-8">
<title>Lakemeadow Creek Veterinary Hospital – Business Card</title>
<link rel="stylesheet" href="https://fonts.googleapis.com/css2?family=Montserrat:wght@400;500;700&display=swap">
<style>
  :root {
    --bg: #2c2e31;
    --card: #ffffff;
    --green: #4a8c3f;
    --green-text: #3f8a2e;
    --brown: #8a6826;
    --grey: #666666;
    --white: #ffffff;
  }
  * { margin: 0; padding: 0; box-sizing: border-box; }
  html, body { width: 1200px; height: 952px; overflow: hidden; }
  body {
    background: var(--bg);
    font-family: "Montserrat", sans-serif;
    display: flex;
    align-items: center;
    justify-content: center;
    gap: 48px;
  }
  .card {
    position: relative;
    width: 540px;
    height: 310px;
    background: var(--card);
    border-radius: 18px;
    overflow: hidden;
  }
  .brand {
    position: absolute;
    display: flex;
    align-items: center;
    gap: 10px;
    color: var(--green-text);
    font-weight: 500;
  }
  .brand-dot {
    width: 14px; height: 14px;
    border-radius: 50%;
    background: var(--green);
    flex: none;
  }
  .brand-name { line-height: 1.2; }
  .front .brand { top: 58px; left: 262px; font-size: 17px; }
  .back .brand { top: 50%; left: 50%; transform: translate(-50%, -50%); font-size: 26px; gap: 14px; }
  .back .brand-dot { width: 20px; height: 20px; }

  .person { position: absolute; top: 34px; left: 26px; }
  .person-name { color: var(--green-text); font-size: 15px; font-weight: 400; letter-spacing: 0.5px; }
  .person-name strong { font-weight: 700; }
  .person-role { color: var(--grey); font-size: 11px; margin-top: 4px; }

  .band { position: absolute; top: 150px; left: 0; right: 0; height: 132px; display: flex; }
  .band-contact {
    width: 200px;
    background: var(--brown);
    color: var(--white);
    font-size: 11px;
    line-height: 1.7;
    padding: 20px 14px 0 26px;
  }
  .band-contact b { font-weight: 700; }
  .band-hours {
    flex: 1;
    background: var(--green);
    color: var(--white);
    text-align: right;
    padding: 22px 26px 0 0;
    font-size: 12px;
    line-height: 1.75;
  }
  .website { margin-top: 6px; letter-spacing: 3px; font-size: 12.5px; }
</style>
</head>
<body>
  <section class="card front">
    <div class="person">
      <p class="person-name">DANIEL R. <strong>HENSLEY</strong></p>
      <p class="person-role">Doctor</p>
    </div>
    <div class="brand">
      <span class="brand-dot"></span>
      <span class="brand-name">Lakemeadow Creek<br>Veterinary Hospital</span>
    </div>
    <div class="band">
      <div class="band-contact">
        <p><b>P :</b> (555) 214-0192</p>
        <p><b>E :</b> info@lmcr.net</p>
        <p>4820 Meadow Creek Lane,<br>Riverton, TX 75010</p>
      </div>
      <div class="band-hours">
        <p>Monday To Friday : 7:00am – 6:00pm</p>
        <p>Saturday: 8:00am – 12:00pm</p>
        <p>Sunday: Closed</p>
        <p class="website">www.lmcr.net</p>
      </div>
    </div>
  </section>

  <section class="card back">
    <div class="brand">
      <span class="brand-dot"></span>
      <span class="brand-name">Lakemeadow Creek<br>Veterinary Hospital</span>
    </div>
  </section>
</body>
</html>
```